Craft beer label required for new modern craft brewery

I require a label to be designed for my craft beer, the name of the beer is "Tidewalker Pale Ale".
It has to be a contemporary style label targeting an audience group between the ages of 21-40. It must be unique and appealing.
The label must incorporate the image of a Gladiator which has to originally created (I’m giving you creative freedom), not copied (for copy right reasons). I’m attaching a few examples, please refer to “gladiator1.jpg” and “Gladiator2.jpg”.
It would be nice if the Vandrello could appear in the background, also originally created I’m attaching an example, please refer to “Vandrello1.jpg”
The Label must also incorporate the attached logo “Fennmoor Brewing Co. Craft Beer-01.jpg” .
The label must fit a 440ml bottle
Please use creative freedom with regards to the shape of the label.
The colours do not have to be exactly the same as logo, but obviously they must match.
Updates

Target Market(s)

Modern/contemporary successful 21-40 year olds

Industry/Entity Type

Brewery

Font styles to use
Serif
Script

Colors

Designer to choose colors to be used in the design.

Requirements
Must have
• My logo, the beer name and the image of a gladiator
• The label size should be at least 10cm wide x 9cm wide.
• The label must include the size of the bottle: 440ml
• The label must include 6.5% ALC./VOL.
Nice to have
• Vandrello in the back ground
Should not have
• Copied images or trade marks

```html
<!DOCTYPE html>
<html lang="en">
<head>
<meta charset="utf-8">
<title>Tidewalker Pale Ale – Label</title>
<link rel="stylesheet" href="https://fonts.googleapis.com/css2?family=Big+Shoulders+Display:wght@800&display=swap">
<style>
  :root {
    --backdrop: #f3e6e6;
    --label-white: #ffffff;
    --ink: #111111;
    --wood-light: #d99a2b;
    --wood-dark: #9a6417;
    --art-gold: #c9a64a;
    --art-grey: #8d8d8d;
    --crest-red: #8e1b2a;
  }
  html, body {
    margin: 0;
    width: 1200px;
    height: 1200px;
    overflow: hidden;
    background: var(--backdrop);
    font-family: "Big Shoulders Display", "Arial Narrow", sans-serif;
  }
  .label {
    position: absolute;
    left: 300px;
    top: 128px;
    width: 600px;
    height: 945px;
    background: var(--label-white);
    overflow: hidden;
    box-shadow: 0 6px 24px rgba(0,0,0,0.08);
  }
  .label-graphics {
    position: absolute;
    inset: 0;
  }
  .wood-panel {
    position: absolute;
    left: 118px;
    top: 0;
    width: 337px;
    height: 400px;
    background: linear-gradient(90deg, var(--wood-dark), var(--wood-light) 30%, var(--wood-dark) 55%, var(--wood-light) 80%, var(--wood-dark));
  }
  .top-rule {
    position: absolute;
    left: 0;
    right: 0;
    top: 54px;
    height: 12px;
    background: var(--ink);
  }
  .brand-mark {
    position: absolute;
    top: 28px;
    left: 50%;
    transform: translateX(-50%);
    display: flex;
    align-items: center;
    gap: 8px;
    background: var(--ink);
    color: var(--label-white);
    padding: 10px 16px;
    border-radius: 34px;
    font-size: 20px;
    letter-spacing: 1px;
    text-transform: uppercase;
    white-space: nowrap;
  }
  .brand-mark .brand-dot {
    width: 14px;
    height: 14px;
    border-radius: 50%;
    background: var(--label-white);
  }
  .beer-name {
    position: absolute;
    left: 70px;
    right: 90px;
    top: 140px;
    margin: 0;
    text-align: center;
    font-size: 80px;
    line-height: 1;
    color: var(--ink);
    letter-spacing: 1px;
    text-transform: uppercase;
  }
  .beer-style {
    position: absolute;
    right: 90px;
    top: 225px;
    margin: 0;
    font-size: 70px;
    line-height: 1;
    color: var(--ink);
    letter-spacing: 6px;
    text-transform: uppercase;
  }
  .hero-art {
    position: absolute;
    left: 64px;
    top: 400px;
    width: 472px;
    height: 472px;
    border-radius: 50%;
    border: 3px solid var(--ink);
    box-sizing: border-box;
    background:
      radial-gradient(circle at 45% 15%, var(--crest-red) 0 6%, transparent 7%),
      radial-gradient(circle at 70% 55%, var(--art-gold) 0 22%, transparent 23%),
      radial-gradient(ellipse at 42% 55%, var(--art-grey) 0 28%, transparent 29%),
      linear-gradient(180deg, #ffffff 40%, #eee2c4 100%);
  }
  .bottle-size, .abv {
    position: absolute;
    bottom: 28px;
    margin: 0;
    font-size: 24px;
    color: var(--ink);
    letter-spacing: 1px;
    text-transform: uppercase;
  }
  .bottle-size { left: 42px; }
  .abv { right: 34px; }
</style>
</head>
<body>
  <main class="label">
    <div class="wood-panel" role="img" aria-label="Vertical wooden plank texture"></div>
    <svg class="label-graphics" width="600" height="945" viewBox="0 0 600 945" aria-hidden="true">
      <line class="cross-band" x1="-20" y1="505" x2="620" y2="770" stroke="#111111" stroke-width="95"/>
      <line class="cross-band" x1="-20" y1="770" x2="620" y2="505" stroke="#111111" stroke-width="95"/>
    </svg>
    <div class="top-rule"></div>
    <div class="brand-mark"><span class="brand-dot"></span>Fennmoor Brewing Co.</div>
    <h1 class="beer-name">Tidewalker</h1>
    <p class="beer-style">Pale Ale</p>
    <div class="hero-art" role="img" aria-label="Illustration of a gladiator in a crested helmet with sword and arrow-struck shield, the Vandrello arena behind him"></div>
    <p class="bottle-size">440/ml</p>
    <p class="abv">6.5% Alc./Vol</p>
  </main>
</body>
</html>
```